Bramble Fitness Business Card - I want exactly the same font than the font on the logo for my Name if possible and address and ETC. or a similar font that will look really good

I need those business cards ASAP so it would be amazing if you can submit your designs as quickly as possible!

Thanks so much

Industry/Entity Type

Business

```html
<!DOCTYPE html>
<html lang="en">
<head>
<meta charset="utf-8">
<title>Bramble Fitness Business Cards</title>
<link href="https://fonts.googleapis.com/css2?family=Michroma&display=swap" rel="stylesheet">
<style>
  :root {
    --sheet: #000000;
    --card: #d3d4d6;
    --ink: #1a1a1a;
    --accent: #c6343b;
  }
  * { margin: 0; padding: 0; box-sizing: border-box; }
  html, body { width: 1200px; height: 1056px; overflow: hidden; background: var(--sheet); }
  .sheet { position: relative; width: 1200px; height: 1056px; background: var(--sheet); font-family: "Michroma", sans-serif; color: var(--ink); }
  .card { position: absolute; width: 485px; height: 269px; background: var(--card); }
  .card--front { left: 455px; top: 386px; }
  .card--back-trainer { left: 160px; top: 702px; }
  .card--back-director { left: 675px; top: 702px; }

  .brand { position: absolute; display: flex; align-items: center; gap: 10px; font-size: 21px; letter-spacing: 1px; color: var(--ink); white-space: nowrap; line-height: 1; }
  .brand__square { width: 16px; height: 16px; background: var(--accent); flex: none; }
  .card--front .brand { left: 0; right: 0; top: 122px; justify-content: center; }

  .brand--side { left: 22px; top: 124px; font-size: 14px; gap: 8px; }
  .brand--side .brand__square { width: 12px; height: 12px; }

  .divider { position: absolute; left: 250px; top: 29px; width: 3px; height: 212px; background: var(--ink); }

  .details { position: absolute; left: 272px; top: 55px; width: 200px; }
  .details__brand { font-size: 12.5px; letter-spacing: 0.5px; color: var(--ink); line-height: 1; margin-bottom: 32px; white-space: nowrap; }
  .details__group { font-size: 6.4px; line-height: 9.6px; margin-bottom: 9.6px; white-space: nowrap; }
</style>
</head>
<body>
<main class="sheet">

  <section class="card card--front" aria-label="Card front">
    <div class="brand"><span class="brand__square"></span><span class="brand__name">BRAMBLE FITNESS</span></div>
  </section>

  <section class="card card--back-trainer" aria-label="Card back, trainer">
    <div class="brand brand--side"><span class="brand__square"></span><span class="brand__name">BRAMBLE FITNESS</span></div>
    <div class="divider"></div>
    <div class="details">
      <p class="details__brand">BRAMBLE FITNESS</p>
      <p class="details__group">Mara Lind<br>Registered Personal Trainer,</p>
      <p class="details__group">Mobile: 0400 218 547<br>mara@bramblefitness.com<br>social.bramblefitness.com</p>
      <p class="details__group">Harbour Point - Australia<br>Level 4<br>88 Quarry Street<br>Melbourne VIC 3000</p>
      <p class="details__group">ABN: 41602958317</p>
    </div>
  </section>

  <section class="card card--back-director" aria-label="Card back, director">
    <div class="brand brand--side"><span class="brand__square"></span><span class="brand__name">BRAMBLE FITNESS</span></div>
    <div class="divider"></div>
    <div class="details">
      <p class="details__brand">BRAMBLE FITNESS</p>
      <p class="details__group">Julien Marchand<br>Director,</p>
      <p class="details__group">Mobile: 0400 736 912<br>julien@bramblefitness.com<br>social.bramblefitness.com</p>
      <p class="details__group">Harbour Point - Australia<br>Level 4<br>88 Quarry Street<br>Melbourne VIC 3000</p>
      <p class="details__group">ABN: 41602958317</p>
    </div>
  </section>

</main>
</body>
</html>
```